Stylish, Masculine Design - Men's Clothing

Halden Suit Depot is a 14,000 square foot warehouse outlet store open to the public since 2005. 50+ brands. Well-known designer brand names and private labels. 30-80% off retail everyday. Lowest prices guaranteed. Average suit price $150. Average shirt price $20. One-stop shop shopping. Men's suits, tuxedos, tuxedo rentals, dress shirts, ties, dress shoes, boy's suits and tuxedos, clergy robes, clergy shirts, cologne, loungewear. Slim fits (Prom Dance), business styles, "church" fashion, security-related uniform. Alterations done by expert tailors on premises for an extra charge.
The final design for both business card and logo should portray stylishness and masculinity.
Updates
We will be changing our name. Details below.New name: Warehouse Suit & TuxFormer name: Halden Suit Depot Added Monday, December 26, 2016
Target Market(s)
Gender: 80% Male, 15% Female, 5% Transgender
Location: 80% 10 Mile Radius, 20% >10 Mile Radius
Age: 17-18 (Primarily prom), 18-35 (Primarily Interviews and Weddings), 36-70 (primarily Church and events)
Race: African-American 50%, Latino-American 20%, White 15%, 10% Asian 5% Other
Religions: Christian 50%, 20% Catholic, 10% Mormon, 20% Other/None
Occupation: Local government 40%, Large corporation employee 20%, Small business employee 10%, Small business owner 10%, 20% Unemployed (high school, college)
Education: High School or equivalent 40%, College 30%, Some College 20%, Masters/Doctors 10%
Industry/Entity Type
Retail
Contact Information for Business Card
Name: Peter Olund
Title: Sales Associate
Address: 418 E. Mirabeth Ave. Larkfield, OR 97411
Phone Number: 541.555.0182
Slogan: Broad Selection. Fair Prices, Friendly Service
www.granarycoatmart.example
Logo Text
GCM (Acronym for Halden Suit Depot) or Image
Requirements
Must have
- Easy to read
- Visually appealing

```html
<!DOCTYPE html>
<html lang="en">
<head>
<meta charset="utf-8">
<title>Halden Suit Depot — Business Card</title>
<link href="https://fonts.googleapis.com/css2?family=Lato:wght@400;700&family=Playfair+Display:wght@700&display=swap" rel="stylesheet">
<style>
  :root{
    --backdrop:#3a3f3d;
    --card-white:#f4f4f2;
    --card-black:#0d0d0d;
    --card-black-soft:#1c1c1c;
    --accent:#e0124f;
    --accent-dark:#9e0d38;
    --ink:#2a2a2a;
    --text-light:#e6e6e6;
    --text-muted:#b5b5b5;
    --icon-bg:#e8e8e8;
  }
  html,body{margin:0;padding:0;width:1200px;height:900px;overflow:hidden;background:var(--backdrop);}
  .canvas{position:relative;width:1200px;height:900px;}
  .card{
    position:absolute;left:100px;top:164px;width:1000px;height:572px;
    background:linear-gradient(160deg,var(--card-black-soft),var(--card-black) 60%);
    box-shadow:0 18px 40px rgba(0,0,0,.45);
    font-family:'Lato',sans-serif;overflow:hidden;
  }
  .card__top{position:absolute;left:0;top:0;width:100%;height:172px;background:var(--card-white);}
  .card__stripe{position:absolute;left:0;top:172px;width:100%;height:12px;
    background:linear-gradient(var(--accent),var(--accent) 70%,var(--accent-dark));}
  .brand{position:absolute;right:60px;top:46px;display:flex;align-items:center;gap:14px;}
  .brand__mark{width:44px;height:44px;background:var(--accent);flex:none;}
  .brand__text{display:flex;flex-direction:column;}
  .brand__name{font-family:'Lato',sans-serif;font-weight:700;font-size:38px;line-height:1;color:var(--ink);letter-spacing:.5px;}
  .brand__slogan{font-family:'Playfair Display',serif;font-weight:700;font-size:13px;color:var(--ink);margin-top:8px;}
  .person{position:absolute;left:60px;top:222px;}
  .person__name{font-size:36px;color:var(--text-light);text-transform:uppercase;letter-spacing:.5px;line-height:1;}
  .person__title{font-size:18px;color:var(--text-muted);text-transform:uppercase;margin-top:6px;}
  .contacts{position:absolute;top:332px;list-style:none;margin:0;padding:0;}
  .contacts--left{left:60px;}
  .contacts--right{left:470px;}
  .contacts li{display:flex;align-items:center;gap:16px;height:38px;font-size:23px;color:var(--text-light);white-space:nowrap;}
  .icon{width:26px;height:26px;flex:none;}
</style>
</head>
<body>
<div class="canvas">
  <div class="card">
    <div class="card__top"></div>
    <div class="card__stripe"></div>

    <div class="brand">
      <div class="brand__mark"></div>
      <div class="brand__text">
        <span class="brand__name">Halden Suit Depot</span>
        <span class="brand__slogan">Broad Selection. Fair Prices, Friendly Service</span>
      </div>
    </div>

    <div class="person">
      <div class="person__name">Peter Olund</div>
      <div class="person__title">Sales Associate</div>
    </div>

    <ul class="contacts contacts--left">
      <li>
        <svg class="icon" viewBox="0 0 26 26"><rect width="26" height="26" rx="5" fill="var(--icon-bg)"/><path d="M8 6c1 0 2 2.5 2 3.3s-1.2 1.2-1 2c.6 1.8 2 3.2 3.8 3.8.8.2 1.2-1 2-1s3.2 1 3.2 2-1 2.9-2.5 2.9C10 19 7 15.9 6 10.5 5.8 8 7 6 8 6z" fill="var(--card-black)"/></svg>
        541.555.0182
      </li>
      <li>
        <svg class="icon" viewBox="0 0 26 26"><rect width="26" height="26" rx="5" fill="var(--icon-bg)"/><rect x="8" y="5" width="10" height="16" rx="2" fill="none" stroke="var(--card-black)" stroke-width="2"/><circle cx="13" cy="18" r="1" fill="var(--card-black)"/></svg>
        (99) 555 018 299
      </li>
      <li>
        <svg class="icon" viewBox="0 0 26 26"><rect width="26" height="26" rx="5" fill="var(--icon-bg)"/><path d="M13 4a6 6 0 0 0-6 6c0 4.5 6 12 6 12s6-7.5 6-12a6 6 0 0 0-6-6z" fill="var(--card-black)"/><circle cx="13" cy="10" r="2.2" fill="var(--icon-bg)"/></svg>
        418 E. Mirabeth Ave. Larkfield, OR 97411
      </li>
    </ul>

    <ul class="contacts contacts--right">
      <li>
        <svg class="icon" viewBox="0 0 26 26"><rect width="26" height="26" rx="5" fill="var(--icon-bg)"/><g fill="none" stroke="var(--card-black)" stroke-width="1.6"><circle cx="13" cy="13" r="7.5"/><ellipse cx="13" cy="13" rx="3.2" ry="7.5"/><path d="M5.5 13h15M7 9h12M7 17h12"/></g></svg>
        haldensuitdepot.example
      </li>
      <li>
        <svg class="icon" viewBox="0 0 26 26"><rect width="26" height="26" rx="5" fill="var(--icon-bg)"/><rect x="6" y="8" width="14" height="10" rx="1.5" fill="none" stroke="var(--card-black)" stroke-width="1.8"/><path d="M6.5 8.5l6.5 5 6.5-5" fill="none" stroke="var(--card-black)" stroke-width="1.8"/></svg>
        info@haldensuitdepot.example
      </li>
    </ul>
  </div>
</div>
</body>
</html>
```